依頼詳細
山形本社にて弊社最大規模の展示会を7月に行います。販売店様用のチラシの作成をお願い致します。商品構成については、ファッション・バッグ・靴・健康ジュエリーなど多数に及びますので、商品コーナー毎の記載をお願い致します。チラシのサイズはA2で4つ折り表裏でお願い致します。
記載項目
社名に関しては、各販売店用として使って頂くので、チラシの裏右下に空欄を設けてもらえると助かります。/展示会名:「ソレイユフェア(仮)」、日時:7/18(金)~7/22(火)9:30~18:00(22日のみ9:30~17:00)、会場:カルデン本社展示場、TEL:023-481-7926、住所:〒990-4127 山形県山形市若葉台5-3-11/各商品写真(添付)、各商品に対しての簡易コメント
サイズ
A2(縦594×横420mm)
ページ数
両面
希望イメージ
シンプル 複雑
単色 カラフル
暗い 明るい
日常 高級
遊び心 厳粛
未来的 伝統的
女性的 男性的
希望する色
赤 黄 緑
納品ファイル
• 高解像度JPG (.jpg)
• イラストレーター形式 (.ai)
補足説明
商品画像については、随時添付させていただきますので、
まずは表紙のデザインだけでもいいので上げていただければ幸いです。
また、「ソレイユフェア」がタイトルなのですが、サブタイトルが未定でございます。
もしよろしければ、サブタイトルも一緒に上げていただければ幸いです。
過去のソレイユフェアの表紙と、去年のソレイユフェアのチラシ構成を添付させていただきますので、
参考にして頂ければ幸いです。何卒宜しくお願い致します。
現在まででチラシに記載する商品画像を添付いたします。

表紙のみでも作成頂ければと思いますので、何卒宜しくお願い致します。

いつものチラシとは違ったデザインであったため、新鮮であったのと、サブタイトルも良かったです。

大変面倒な依頼でしたが、ご提案頂き、ありがとうございました。

```html
<!DOCTYPE html>
<html lang="ja">
<head>
<meta charset="utf-8">
<title>第27回 ソレイユフェア</title>
<link href="https://fonts.googleapis.com/css2?family=Great+Vibes&family=Shippori+Mincho:wght@500;700&family=Noto+Sans+JP:wght@400;500;700&display=swap" rel="stylesheet">
<style>
  :root {
    --lavender-deep: #5b3f8c;
    --lavender: #8a6bbf;
    --lavender-soft: #c9b6e4;
    --gold: #c9a24a;
    --gold-light: #e8cf86;
    --ink: #3a2a5c;
    --paper: #ffffff;
  }
  * { margin: 0; padding: 0; box-sizing: border-box; }
  html, body { width: 846px; height: 1200px; overflow: hidden; background: var(--paper); }
  .flyer { position: relative; width: 846px; height: 1200px; overflow: hidden; background: var(--paper); font-family: "Noto Sans JP", sans-serif; color: var(--ink); }

  .hero-photo {
    position: absolute; left: 0; top: 0; width: 846px; height: 900px;
    background: linear-gradient(180deg, #cfd0dd 0%, #b9b7cf 18%, #6f7a64 30%, #8d74b8 45%, #7b5fae 70%, #6a4c9c 100%);
  }
  .tagline {
    position: absolute; top: 22px; left: 0; width: 100%; text-align: center;
    font-family: "Shippori Mincho", serif; font-weight: 700; font-size: 40px;
    color: var(--paper); letter-spacing: 2px; font-style: italic;
    text-shadow: 0 2px 6px rgba(60,40,100,.35);
  }

  .fair-badge {
    position: absolute; left: 185px; top: 380px; width: 476px; height: 420px;
    background: rgba(255,255,255,.93); border: 5px solid var(--gold);
    border-radius: 90px; box-shadow: 0 0 0 4px rgba(255,255,255,.9), 0 0 0 6px var(--gold-light);
  }
  .crown-mark {
    position: absolute; left: 198px; top: -48px; width: 70px; height: 44px;
    background: linear-gradient(180deg, var(--gold-light), var(--gold)); border-radius: 6px;
  }
  .edition {
    position: absolute; top: 12px; left: 0; width: 100%; text-align: center;
    font-family: "Shippori Mincho", serif; font-weight: 700; font-size: 26px; color: var(--gold);
  }
  .fair-name {
    position: absolute; left: 0; width: 100%; text-align: center;
    font-family: "Great Vibes", cursive; color: var(--gold); line-height: 1;
  }
  .fair-name.first { top: 70px; font-size: 124px; padding-right: 30px; }
  .fair-name.second { top: 250px; font-size: 124px; padding-left: 130px; }
  .fair-kana {
    position: absolute; top: 212px; left: 95px;
    font-family: "Noto Sans JP", sans-serif; font-weight: 700; font-size: 18px; color: var(--lavender-deep);
  }

  .event-info { position: absolute; left: 30px; top: 910px; width: 520px; color: var(--lavender-deep); }
  .event-date { font-weight: 700; font-size: 64px; line-height: 1; letter-spacing: -1px; display: flex; align-items: center; }
  .event-date .unit { font-size: 40px; }
  .event-date .tilde { margin: 0 6px; font-size: 48px; }
  .day-dot {
    display: inline-block; width: 36px; height: 36px; border-radius: 50%;
    background: var(--lavender-deep); color: var(--paper); font-size: 22px; line-height: 36px; text-align: center; margin-left: 4px;
  }
  .event-time { margin-top: 14px; font-weight: 500; font-size: 46px; line-height: 1; }
  .event-time .ampm { font-size: 28px; }
  .event-note { margin-top: 8px; font-size: 22px; font-weight: 500; }
  .event-details { margin-top: 14px; font-size: 21px; line-height: 1.45; color: var(--ink); }

  .venue-map { position: absolute; left: 570px; top: 960px; width: 250px; }
  .venue-map-label { font-size: 14px; font-weight: 700; color: var(--ink); margin-bottom: 4px; }
  .venue-map-area { width: 250px; height: 210px; background: linear-gradient(135deg, #f1eff6, #dcd8e8); border: 1px solid #b7b0cc; }
</style>
</head>
<body>
<main class="flyer">
  <div class="hero-photo" role="img" aria-label="ラベンダー畑に立つ帽子とドレスの女性の写真"></div>
  <p class="tagline">プレミアムな夏を身に纏う</p>

  <section class="fair-badge">
    <div class="crown-mark" role="img" aria-label="王冠の飾り"></div>
    <p class="edition">第27回</p>
    <p class="fair-name first">Soleil</p>
    <p class="fair-kana">ソレイユフェア</p>
    <p class="fair-name second">Fair</p>
  </section>

  <section class="event-info">
    <p class="event-date">7<span class="unit">月</span>18<span class="unit">日</span><span class="day-dot">金</span><span class="tilde">～</span>22<span class="unit">日</span><span class="day-dot">火</span></p>
    <p class="event-time"><span class="ampm">AM</span>9:00～<span class="ampm">PM</span>18:00</p>
    <p class="event-note">(22日のみAM9:30～PM17:00)</p>
    <div class="event-details">
      <p>会場：カルデン本社展示場</p>
      <p>TEL：023-481-7926</p>
      <p>住所：〒990-4127 山形県山形市若葉台5-3-11</p>
    </div>
  </section>

  <aside class="venue-map">
    <p class="venue-map-label">会場案内図</p>
    <div class="venue-map-area" role="img" aria-label="会場周辺の案内地図"></div>
  </aside>
</main>
</body>
</html>
```